Website header design

Need a graphic design for a Wordpress website.

The site is based on a premium theme that client has already selected: - http://demo.plinkastyles.com/?name=corridor

The purpose of this project is to create a header banner that includes the client picture, company name and tag line and an attractive, clean and modern looking background.

For information only: The background of site will be white or a light color

The Header should include the site name: "The Quorvale healing Centre Ltd" and the tag line: "Tap Into Your Fullest Potential"

The client has also provided a color scheme they like( See attachment )

Banner height: 140 Pix

Target Market(s)

The audience of this site are people who are looking for solution to various health issues and consider EFT as a solution.

EFT stands for "Emotional Freedom Technique"

Industry/Entity Type

Graphic Design

Requirements
Must have
• The colors that the client has selected are very bright.
Still I would like the header to have a lot of light in it so that it does not look to bulky.

Results must be provided in a PSD file
Nice to have
• The banner can be constructed from few layers
Should not have
• No specific symbol.

```html
<!DOCTYPE html>
<html lang="en">
<head>
<meta charset="utf-8">
<title>The Quorvale Healing Centre Ltd – Header</title>
<link rel="stylesheet" href="https://fonts.googleapis.com/css2?family=Aladin&family=Noticia+Text:wght@700&display=swap">
<style>
  :root {
    --page-bg: #f2f2f2;
    --frame-blue: #bfe0ea;
    --frame-shadow: rgba(90, 130, 150, 0.45);
    --sky-warm: #fbe7d9;
    --sky-light: #fffaf3;
    --sky-cool: #d9dde6;
    --sky-sun: #fff3dc;
    --title-brown: #a3570f;
    --tagline-teal: #13889f;
    --portrait-border: #d9c8b6;
    --portrait-mat: #f4ece6;
    --portrait-tone: #8a5a44;
  }
  * { margin: 0; padding: 0; box-sizing: border-box; }
  html, body {
    width: 1200px;
    height: 900px;
    overflow: hidden;
    background: var(--page-bg);
  }
  .header-banner {
    position: absolute;
    left: 93px;
    top: 114px;
    width: 971px;
    height: 143px;
    border: 3px solid var(--frame-blue);
    box-shadow: 0 3px 4px var(--frame-shadow);
    overflow: hidden;
  }
  .banner-sky {
    position: absolute;
    inset: 0;
    background:
      radial-gradient(ellipse 180px 70px at 500px 120px, var(--sky-sun), transparent 80%),
      linear-gradient(180deg, var(--sky-light) 0%, var(--sky-warm) 65%, var(--sky-cool) 100%);
  }
  .site-title {
    position: absolute;
    left: 0;
    width: 905px;
    top: 28px;
    text-align: center;
    font-family: "Aladin", fantasy;
    font-size: 38px;
    letter-spacing: 1px;
    color: var(--title-brown);
    white-space: nowrap;
  }
  .site-tagline {
    position: absolute;
    left: 0;
    width: 950px;
    top: 82px;
    text-align: center;
    font-family: "Noticia Text", serif;
    font-weight: 700;
    font-size: 18px;
    letter-spacing: 0.4px;
    color: var(--tagline-teal);
    text-shadow: 0 1px 1px rgba(255, 255, 255, 0.9);
  }
  .portrait-frame {
    position: absolute;
    right: 2px;
    top: 2px;
    width: 110px;
    height: 133px;
    background: var(--portrait-mat);
    border: 3px solid var(--portrait-border);
  }
  .portrait-photo {
    position: absolute;
    left: 4px;
    top: 3px;
    width: 96px;
    height: 121px;
    background: linear-gradient(180deg, var(--portrait-mat) 0%, var(--portrait-tone) 100%);
  }
</style>
</head>
<body>
  <header class="header-banner">
    <div class="banner-sky" role="img" aria-label="Soft sunrise sky with light clouds"></div>
    <h1 class="site-title">THE QUORVALE HEALING CENTRE LTD</h1>
    <p class="site-tagline">Tap into Your Fullest Potencial</p>
    <div class="portrait-frame">
      <div class="portrait-photo" role="img" aria-label="Portrait photo of the practitioner"></div>
    </div>
  </header>
</body>
</html>
```